Buchcover-Design für Ratgeber für Eltern
Zielgruppe
Ich bin promovierte Pädagogin. Das Buch, für das ein Cover benötigt wird (für ebook und Printversion) ist ein Ratgeber für Eltern, die plötzlich mit eine Schreikind nach der Geburt konfrontiert sind. Dafür wird schnelle Hilfe durch Tipps ebenso wie Hintergrundinformationen im Sinne eines Fachbuchs gegeben. Buchtitel: Die Elternbrücke, Autorin: Katrin Brandt, der Untertitel: Fachbuch rund um das Thema 'Schreikind'.
Aufgabenstellung
Das Cover soll Eltern, insbesondere Mütter ansprechen, schnell ins Auge fallen und das Herz ansprechen und auf das Wesentliche reduziert sein, womit die formschöne Aufteilung und passende Schriftart, -farbe sehr wichtig werden. Es gibt ein Covervorbild, das Buch 'Kieselsommer' von Thomas Kern Wallrabe. Die Hintergrundfarbe sollte ein schönes, eher dunkleres pink/himbeer sein. Statt des Welpen sollte ein Babygesicht abgebildet sein. Die Schriftart des Titels sollte etwas weniger verspielt sein.
Ich bräuchte die Datei für ein ebook und später auch für ein Taschenbuch und Hardcover. Dafür ist sind die Breiten für die Buchrücken noch nicht klar. Die entsprechende Datei müsste später nochmals angepasst werden - eventuell auch erst in zwei, drei Monaten - das sollte in dem Auftrag eingeschlossen sein. Später wird eventuell ein angepasste Design für ein Hörbuch nötig, hier wäre die Möglichkeit zu späteren Zusammenarbeit wünschenswert.

```html
<!DOCTYPE html>
<html lang="de">
<head>
<meta charset="utf-8">
<title>Die Elternbrücke – Katrin Brandt</title>
<link rel="stylesheet" href="https://fonts.googleapis.com/css2?family=Roboto:wght@300;400;500&display=swap">
<style>
  :root {
    --raspberry: #c70c45;
    --white: #ffffff;
    --blush: #f4b6c8;
    --ring: #dc5a7d;
    --photo-light: rgba(244, 232, 226, 0.95);
    --photo-mid: rgba(226, 196, 182, 0.85);
    --photo-edge: rgba(199, 12, 69, 0);
  }
  html, body {
    margin: 0;
    padding: 0;
    width: 834px;
    height: 1200px;
    overflow: hidden;
  }
  .cover {
    position: relative;
    width: 834px;
    height: 1200px;
    background: var(--raspberry);
    color: var(--white);
    font-family: "Roboto", Arial, sans-serif;
    overflow: hidden;
  }
  .title {
    position: absolute;
    top: 88px;
    left: 0;
    width: 100%;
    margin: 0;
    text-align: center;
    font-weight: 300;
    line-height: 1;
  }
  .title-article {
    display: block;
    font-size: 58px;
  }
  .title-main {
    display: block;
    margin-top: 8px;
    font-size: 86px;
    letter-spacing: 0.5px;
  }
  .title-rule {
    position: absolute;
    top: 252px;
    left: 232px;
    width: 370px;
    height: 3px;
    background: var(--white);
  }
  .subtitle {
    position: absolute;
    top: 276px;
    left: 0;
    width: 100%;
    margin: 0;
    text-align: center;
    font-weight: 300;
    font-size: 31px;
    line-height: 40px;
    color: var(--blush);
  }
  .rings {
    position: absolute;
    top: 457px;
    left: 155px;
    width: 580px;
    height: 580px;
  }
  .cover-photo {
    position: absolute;
    top: 370px;
    left: 95px;
    width: 680px;
    height: 680px;
    border-radius: 50%;
    background: radial-gradient(closest-side, var(--photo-light) 0%, var(--photo-mid) 55%, var(--photo-edge) 100%);
  }
  .author {
    position: absolute;
    top: 1100px;
    left: 0;
    width: 100%;
    margin: 0;
    text-align: center;
    font-weight: 500;
    font-size: 24px;
    letter-spacing: 1.5px;
  }
</style>
</head>
<body>
  <main class="cover">
    <h1 class="title">
      <span class="title-article">Die</span>
      <span class="title-main">Elternbrücke</span>
    </h1>
    <div class="title-rule"></div>
    <p class="subtitle">Fachbuch rund um das<br>Thema ‘Schreikind’</p>

    <svg class="rings" viewBox="0 0 580 580" aria-hidden="true">
      <circle cx="290" cy="290" r="286" fill="none" stroke="var(--ring)" stroke-width="4"/>
      <circle cx="290" cy="290" r="270" fill="none" stroke="var(--ring)" stroke-width="3"/>
    </svg>

    <div class="cover-photo" role="img" aria-label="Foto eines lächelnden Babys im Pullunder, das auf allen vieren krabbelt, vor einem blütenförmigen Ornament"></div>

    <p class="author">KATRIN BRANDT</p>
  </main>
</body>
</html>
```